Copper Kettle Catering
Business Cards and Letterhead
Copper Kettle Catering -
Creative Brief
Use standard fonts
R Danela Forsythe
Chef/Owner
287 W 93rd St FL2 New York, NY 10025
copperkettlecatering@mailbox.example
copperkettlecatering.example

```html
<!DOCTYPE html>
<html lang="en">
<head>
<meta charset="utf-8">
<title>Copper Kettle Catering – Business Card</title>
<link rel="stylesheet" href="https://fonts.googleapis.com/css2?family=PT+Sans:wght@400;700&display=swap">
<style>
  :root {
    --backdrop: #a3a3a3;
    --card-white: #ffffff;
    --copper-light: #dea046;
    --copper-dark: #c07a22;
    --accent-red: #d3262a;
    --text-light: #ffffff;
    --text-dark: #4a2a0e;
  }
  html, body {
    margin: 0;
    padding: 0;
    width: 1200px;
    height: 458px;
    overflow: hidden;
    background: var(--backdrop);
    font-family: "PT Sans", Arial, sans-serif;
  }
  .canvas {
    position: relative;
    width: 1200px;
    height: 458px;
  }
  .card {
    position: absolute;
    top: 56px;
    width: 498px;
    height: 342px;
    overflow: hidden;
  }
  .card--front { left: 72px; }
  .card--back {
    left: 630px;
    background: linear-gradient(135deg, var(--copper-light), var(--copper-dark));
  }
  .card__art {
    position: absolute;
    inset: 0;
    width: 100%;
    height: 100%;
  }
  .contact {
    position: absolute;
    right: 22px;
    top: 18px;
    text-align: right;
    color: var(--text-light);
  }
  .contact__name {
    font-size: 17px;
    font-weight: 700;
    margin: 0;
  }
  .contact__role {
    font-size: 12px;
    font-weight: 700;
    margin: 4px 0 0;
  }
  .contact__address {
    font-size: 14px;
    line-height: 19px;
    margin: 78px 12px 0 0;
    font-style: normal;
  }
  .contact__line {
    position: relative;
    display: block;
    font-size: 14px;
    line-height: 19px;
    margin-right: 12px;
  }
  .contact__line::after {
    content: "";
    position: absolute;
    right: -13px;
    top: 6px;
    width: 7px;
    height: 7px;
    background: var(--accent-red);
  }
  .contact__phones { margin-top: 10px; }
  .contact__web { margin-top: 10px; }
  .wordmark {
    position: absolute;
    font-weight: 700;
    color: var(--text-dark);
    margin: 0;
    line-height: 1.05;
  }
  .card--front .wordmark {
    left: 40px;
    top: 120px;
    font-size: 30px;
    width: 220px;
  }
  .card--back .wordmark {
    left: 0;
    right: 0;
    top: 120px;
    text-align: center;
    font-size: 44px;
  }
  .back__web {
    position: absolute;
    left: 0;
    right: 0;
    bottom: 26px;
    text-align: center;
    font-size: 15px;
    font-weight: 700;
    color: var(--text-dark);
    margin: 0;
  }
</style>
</head>
<body>
<main class="canvas">
  <section class="card card--front" aria-label="Business card front">
    <svg class="card__art" viewBox="0 0 498 342" preserveAspectRatio="none" aria-hidden="true">
      <defs>
        <linearGradient id="copperFill" x1="0" y1="0" x2="1" y2="1">
          <stop offset="0" stop-color="var(--copper-light)"/>
          <stop offset="1" stop-color="var(--copper-dark)"/>
        </linearGradient>
      </defs>
      <rect width="498" height="342" fill="var(--card-white)"/>
      <path d="M262 0 C 190 60, 300 160, 160 230 C 90 265, 50 300, 40 342 L498 342 L498 0 Z" fill="url(#copperFill)"/>
      <path d="M250 0 C 178 60, 288 160, 148 230 C 78 265, 38 300, 28 342" fill="none" stroke="var(--accent-red)" stroke-width="6"/>
    </svg>
    <p class="wordmark">Copper Kettle Catering</p>
    <div class="contact">
      <p class="contact__name">R Danela Forsythe</p>
      <p class="contact__role">Chef/Owner</p>
      <address class="contact__address">287 W 93rd St FL2<br>New York, NY 10025</address>
      <div class="contact__phones">
        <span class="contact__line">555.014.3827</span>
        <span class="contact__line">555.019.6410</span>
      </div>
      <div class="contact__web">
        <span class="contact__line">copperkettlecatering@mailbox.example</span>
        <span class="contact__line">copperkettlecatering.example</span>
      </div>
    </div>
  </section>

  <section class="card card--back" aria-label="Business card back">
    <p class="wordmark">Copper Kettle Catering</p>
    <p class="back__web">www.copperkettlecatering.example</p>
  </section>
</main>
</body>
</html>
```